Marwick Placement & Skills Service (M.P.S.S.)

Company brochure, just to look more professional than I have it now.
To get a better understanding of my company, I have put together a mock brochure and power point presentation. You can also look at my website www.hirepathnow.example. That should help you out a lot. After my brochure is complete, I will update my website so they match. Thanks
Any questions, please call. 555-0142-3377

Target Market(s)

I target both employers and state agency's

Industry/Entity Type

It Company

Font styles to use
Sans Serif

Colors
6a429a

Requirements
Must have
• Wording that is in the sample except for the reply page, that can be taken off
• All of my contact information (address, phone number, office number, fax number email and website. My Logo - Colors are purple, gray . Nothing below a 12 pt font (I service blind consumers too)
• I want to be able to mail it so I like the back middle page, I just want it to look more professional. The order of the panels does not matter
Nice to have
• Civic benefit pathway to careers logo and Lone Plains Labor Bureau logo. If you need a better on, you can get it from their web sites
Should not have
• I work with individuals that are disabled and help them find a job in the community where they can be useful and feel good about themself. So nothing that can be offensive to any race, orientation, gender, etc.

```html
<!DOCTYPE html>
<html lang="en">
<head>
<meta charset="utf-8">
<title>Marwick Placement &amp; Skills Service – Brochure Outside</title>
<link href="https://fonts.googleapis.com/css2?family=Cabin:ital,wght@0,400;0,500;0,600;1,400&display=swap" rel="stylesheet">
<style>
  :root{
    --purple:#4c3b96;
    --purple-soft:#6a429a;
    --grey:#9a9ca3;
    --grey-light:#d4d5d8;
    --ink:#1d1d22;
    --paper:#ffffff;
    --bg:#e6e6e8;
  }
  *{box-sizing:border-box;margin:0;padding:0}
  html,body{width:1200px;height:1200px;overflow:hidden;background:var(--bg);font-family:"Cabin",sans-serif;color:var(--ink)}
  .brochure{position:absolute;left:45px;top:170px;width:1110px;height:860px;display:flex;box-shadow:0 12px 30px rgba(0,0,0,.18)}
  .panel{position:relative;width:370px;height:860px;background:var(--paper);overflow:hidden}
  .panel + .panel{border-left:1px solid #ececef}
  .deco{position:absolute;left:0;top:0;width:370px;height:860px}
  .photo{position:absolute;border-radius:50%;border:9px solid var(--purple);box-shadow:0 0 0 5px #fff,0 4px 10px rgba(0,0,0,.2)}

  /* Services panel */
  .services-intro{position:absolute;top:32px;left:24px;right:24px;text-align:center;font-size:15px;line-height:1.35}
  .services-intro .lead{color:var(--purple);font-size:20px;text-decoration:underline;display:block;margin-bottom:4px}
  .method-band{position:absolute;top:184px;left:0;right:0;height:86px;background:var(--purple);color:#fff;font-size:15px;font-style:italic;text-align:center;padding:12px 30px;line-height:1.35}
  .photo-team{left:85px;top:292px;width:230px;height:230px;background:linear-gradient(135deg,#d9dfe6,#6f7d92 60%,#2c3445)}
  .photo-puzzle{left:190px;top:505px;width:130px;height:130px;background:linear-gradient(160deg,#eef0f2,#9aa1ab 55%,#3b3f48)}
  .program-title{position:absolute;left:26px;top:652px;font-variant:small-caps;font-size:26px;font-weight:500;line-height:1.15;color:var(--ink)}
  .program-title .initial{color:var(--purple);font-size:32px}
  .program-title span.line{display:block}
  .program-title span.line:nth-child(2){padding-left:14px}
  .program-title span.line:nth-child(3){padding-left:2px}

  /* Mailer panel */
  .panel-mailer{background:linear-gradient(160deg,#ffffff 0%,#f1f1f3 45%,#e9e9ec 60%,#ffffff 100%)}
  .return-address,.return-web{position:absolute;writing-mode:vertical-rl;font-size:13px;line-height:1.5;color:var(--ink)}
  .return-address{right:40px;top:30px}
  .return-web{left:48px;top:30px}
  .mailer-mark{position:absolute;left:60px;top:610px;writing-mode:vertical-rl;display:flex;align-items:center;gap:10px;color:var(--purple);font-size:20px;font-weight:500}
  .mark-dot{width:22px;height:22px;border-radius:50%;background:var(--grey)}
  .stamp{position:absolute;right:55px;top:680px;width:110px;height:110px;background:var(--grey-light)}

  /* Cover panel */
  .brand{position:absolute;top:50px;left:0;right:0;display:flex;justify-content:center;align-items:center;gap:12px;color:var(--purple);font-size:36px;font-weight:500;letter-spacing:3px}
  .brand .mark-dot{width:30px;height:30px}
  .cover-title{position:absolute;top:130px;left:30px;right:20px;font-size:29px;line-height:1.15;text-align:center}
  .cover-title .accent{color:var(--purple);display:block}
  .photo-portrait{left:45px;top:290px;width:280px;height:280px;background:radial-gradient(circle at 45% 40%,#f1ddd0,#c9a58f 45%,#3d3b40 85%)}
  .tagline-band{position:absolute;top:606px;left:0;right:0;height:92px;background:var(--purple);color:#fff;font-size:16.5px;text-align:center;padding:12px 18px;line-height:1.4}
  .contact{position:absolute;top:710px;left:20px;right:18px;font-size:13.5px;line-height:1.45;display:grid;grid-template-columns:auto auto;justify-content:space-between;column-gap:10px}
  .contact .phones{grid-column:1 / 3;margin-top:8px;text-align:center}
</style>
</head>
<body>
<main class="brochure">

  <section class="panel panel-services">
    <svg class="deco" viewBox="0 0 370 860" aria-hidden="true">
      <path d="M0 330 Q40 560 150 660 Q250 750 370 770" fill="none" stroke="var(--grey-light)" stroke-width="2"/>
      <path d="M0 760 Q190 760 370 820 L370 860 L0 860 Z" fill="var(--purple)"/>
    </svg>
    <p class="services-intro">
      <span class="lead">Personalized</span>
      Job Readiness Training,<br>
      Job Coaching, Job Placement<br>
      and Supportive Employment Services.<br>
      All using a proven curriculum, advance training<br>
      and coaching.
    </p>
    <p class="method-band">Methods that have successfully helped hundreds of individual learn how to find and maintain employment.</p>
    <div class="photo photo-team" role="img" aria-label="Photo of a smiling businessman at a meeting table with a colleague"></div>
    <div class="photo photo-puzzle" role="img" aria-label="Photo of a professional holding a puzzle piece"></div>
    <h2 class="program-title">
      <span class="line"><span class="initial">C</span>ommunity</span>
      <span class="line"><span class="initial">R</span>ehabilitation</span>
      <span class="line"><span class="initial">P</span>rogram</span>
    </h2>
  </section>

  <section class="panel panel-mailer">
    <p class="return-address">Marwick Placement &amp; Skills Service<br>Office: 482 Meridian Loop #210 Fairhaven, ST 00412</p>
    <p class="return-web">Web: www.hirepathnow.example<br>Email: hirepathnow@mail.example</p>
    <div class="mailer-mark"><span>M.P.S.S.</span><span class="mark-dot"></span></div>
    <div class="stamp" aria-label="Postage area"></div>
  </section>

  <section class="panel panel-cover">
    <svg class="deco" viewBox="0 0 370 860" aria-hidden="true">
      <path d="M0 380 Q60 280 185 278 Q300 276 370 330 L370 360 Q290 300 185 300 Q80 300 20 400 Z" fill="var(--purple)"/>
      <path d="M0 830 Q180 810 370 850 L370 860 L0 860 Z" fill="var(--purple)"/>
    </svg>
    <div class="brand"><span class="mark-dot"></span><span>M.P.S.S.</span></div>
    <h1 class="cover-title">Marwick Placement<span class="accent">&amp; Skills Service</span></h1>
    <div class="photo photo-portrait" role="img" aria-label="Portrait photo of a smiling professional in an office"></div>
    <p class="tagline-band">A Community Rehabilitation Program &amp; Employment Network w/ Civic Benefit Pathway</p>
    <div class="contact">
      <p>482 Meridian Loop #210<br>Fairhaven, ST 00412</p>
      <p>hirepathnow@mail.example<br>www.hirepathnow.example</p>
      <p class="phones">Office: (555) 014-2210 | Ms. M's 555-0142-3377<br>Fax: (555) 014-2291</p>
    </div>
  </section>

</main>
</body>
</html>
```